Events floral designer business needs a logo design

I need a logo design for my floral design business called tender thistles.
i am inspired by nature and the simplicity of its beauty, whilst upcycling and recycling materials to reduce waste and impact on our environment.
I would like the design to be printed on recycled brown cardboard so i would like a simple but striking design of a bold black ivy vine or gnarly magnolia or tree branch with lower case old school type writer font.

Target Market(s)

Anyone requiring floral additions for their event

Industry/Entity Type

Business

Contact Information for Business Card

rosa kettering
floral designer/creator
0461807352
rosa@tenderthistles.com
tenderthistles.com

Font styles to use
Other font styles liked:
• lower case type writer

Colors
000000

Requirements
Must have
• simplicity but boldness
• Black typewriter font and bold picture with my details
Nice to have
• as above
Should not have
• colour

```html
<!DOCTYPE html>
<html lang="en">
<head>
<meta charset="utf-8">
<title>tender thistles — business card</title>
<link rel="stylesheet" href="https://fonts.googleapis.com/css2?family=Special+Elite&display=swap">
<style>
  :root {
    --backdrop: #121212;
    --kraft: #a38d70;
    --kraft-light: #b19c7f;
    --kraft-dark: #8f7a5f;
    --ink: #111010;
  }
  * { box-sizing: border-box; margin: 0; padding: 0; }
  html, body {
    width: 1200px;
    height: 1200px;
    overflow: hidden;
    background: var(--backdrop);
  }
  .canvas {
    width: 1200px;
    height: 1200px;
    display: flex;
    flex-direction: column;
    align-items: center;
    justify-content: center;
    gap: 70px;
  }
  .card {
    position: relative;
    width: 840px;
    height: 480px;
    border-radius: 40px;
    background:
      radial-gradient(ellipse at 30% 35%, var(--kraft-light) 0%, transparent 60%),
      radial-gradient(ellipse at 80% 80%, var(--kraft-dark) 0%, transparent 55%),
      var(--kraft);
    color: var(--ink);
    font-family: "Special Elite", "Courier New", monospace;
    text-transform: lowercase;
  }
  .rule {
    position: absolute;
    height: 2px;
    width: 120px;
    background: var(--ink);
  }
  /* front */
  .card-front .rule-top { top: 120px; left: 520px; }
  .card-front .rule-bottom { top: 350px; left: 300px; }
  .brand {
    position: absolute;
    top: 170px;
    left: 0;
    width: 100%;
    display: flex;
    align-items: center;
    justify-content: center;
    gap: 26px;
  }
  .brand-mark {
    width: 70px;
    height: 70px;
    border-radius: 50%;
    background: var(--ink);
  }
  .brand-name {
    font-size: 40px;
    letter-spacing: 0.14em;
  }
  /* back */
  .card-back .rule-top { top: 80px; left: 420px; }
  .card-back .rule-bottom { top: 380px; left: 170px; }
  .contact {
    position: absolute;
    top: 140px;
    left: 170px;
    width: 400px;
    text-align: center;
    font-size: 24px;
    line-height: 1.35;
    letter-spacing: 0.06em;
  }
  .contact .person { font-size: 27px; letter-spacing: 0.12em; }
</style>
</head>
<body>
  <main class="canvas">
    <section class="card card-front" aria-label="business card front">
      <span class="rule rule-top"></span>
      <div class="brand">
        <span class="brand-mark"></span>
        <span class="brand-name">tender thistles</span>
      </div>
      <span class="rule rule-bottom"></span>
    </section>

    <section class="card card-back" aria-label="business card back">
      <span class="rule rule-top"></span>
      <address class="contact" style="font-style: normal;">
        <p class="person">rosa kettering</p>
        <p class="role">floral designer/creator</p>
        <p class="phone">0461807352</p>
        <p class="email">rosa@tenderthistles.com</p>
        <p class="web">tenderthistles.com</p>
      </address>
      <span class="rule rule-bottom"></span>
    </section>
  </main>
</body>
</html>
```